Book Cover Design - Uncovering Weight Loss Secrets

I need a book cover design for a book called 'Folding The Map'. It is a book that goes through all of the secrets to weight loss, without any crazy shakes or workouts or pills or potions. The book is really focused on helping people understand that Weight loss is simple and has more to do with our mindset as well as the food we were eating. It is about taking personal responsibility not looking for the next fancy revolutionary product that is going to help them magically melt the fat away. The book is pragmatic in nature and breaks down in simple terms how we can lose weight and keep it off for the rest of our lives. It shows the user that it is simple to lose weight, but it takes effort. They should stop looking for a quick fix when it comes to weight loss but instead eat healthy for the rest of their lives.
The book is intended to be hard-hitting no holds barred approach. The book has the same title as my business name. I will attach the current logo that we use in the business. This doesn't need to be on the front of the book maybe at the back down the bottom somewhere.
I am looking to have both an e-book cover and a standard printed book cover.
I don't have any colours in mind, my logo can be adapted to be different colours or just white.
The message that I am wanting people to feel when they see my book, is that all these Weightloss fads are a joke, that I know the secrets that will get them to their weight loss goal even if they fail at everything else before.
On the cover it should say the following.
FOLDING THE MAP
Uncovering the Weight Loss Secrets
The big companies have been trying to keep hidden for years!
COLIN MAYHEW
People who have failed many times trying to lose weight & need help
Weight Loss

```html
<!DOCTYPE html>
<html lang="en">
<head>
<meta charset="utf-8">
<title>Folding The Map — Colin Mayhew</title>
<link rel="stylesheet" href="https://fonts.googleapis.com/css2?family=Anton&family=Oswald:wght@700&display=swap">
<style>
  :root {
    --backdrop: #cfcfcf;
    --paper: #ffffff;
    --navy: #003470;
    --sky: #3a87b5;
    --photo-light: #f7f7f5;
    --photo-fruit: #e9d98a;
    --photo-blue: #7fb2d6;
    --photo-green: #a9c46a;
  }
  html, body {
    margin: 0;
    width: 1200px;
    height: 1200px;
    overflow: hidden;
    background: var(--backdrop);
  }
  .book-cover {
    position: absolute;
    left: 220px;
    top: 30px;
    width: 760px;
    height: 1140px;
    background: var(--paper);
  }
  .book-cover svg { display: block; width: 100%; height: 100%; }
  .title { font-family: "Anton", "Oswald", sans-serif; }
  .title-top { fill: var(--navy); font-size: 148px; }
  .title-bottom { fill: var(--sky); font-size: 158px; }
  .subtitle { font-family: "Oswald", "Arial Narrow", sans-serif; font-weight: 700; }
  .subtitle-lead { fill: var(--sky); font-size: 49px; }
  .subtitle-tail { fill: var(--navy); font-size: 35px; }
  .author-band { fill: var(--sky); }
  .author-name { fill: var(--paper); font-family: "Oswald", "Arial Narrow", sans-serif; font-weight: 700; font-size: 41px; }
</style>
</head>
<body>
  <main class="book-cover">
    <svg viewBox="0 0 760 1140" xmlns="http://www.w3.org/2000/svg">
      <defs>
        <linearGradient id="still-life" x1="0" y1="0" x2="1" y2="0.4">
          <stop offset="0" stop-color="var(--photo-green)" stop-opacity="0.55"/>
          <stop offset="0.35" stop-color="var(--photo-fruit)" stop-opacity="0.7"/>
          <stop offset="0.65" stop-color="var(--photo-blue)" stop-opacity="0.7"/>
          <stop offset="1" stop-color="var(--photo-light)"/>
        </linearGradient>
      </defs>

      <rect class="cover-photo" x="0" y="364" width="760" height="444" fill="url(#still-life)" role="img" aria-label="Photo of fruit smoothies, apples, bananas and kiwi beside blue dumbbells and a yellow measuring tape"/>

      <text class="title title-top" x="72" y="192" textLength="622" lengthAdjust="spacingAndGlyphs">FOLDING</text>
      <text class="title title-bottom" x="92" y="352" textLength="600" lengthAdjust="spacingAndGlyphs">THE MAP</text>

      <text class="subtitle subtitle-lead" x="380" y="883" text-anchor="middle" textLength="304" lengthAdjust="spacingAndGlyphs">UNCOVERING</text>
      <text class="subtitle subtitle-lead" x="387" y="935" text-anchor="middle" textLength="592" lengthAdjust="spacingAndGlyphs">THE WEIGHT LOSS SECRETS</text>
      <text class="subtitle subtitle-tail" x="386" y="980" text-anchor="middle" textLength="611" lengthAdjust="spacingAndGlyphs">THE BIG COMPANIES HAVE BEEN TRYING</text>
      <text class="subtitle subtitle-tail" x="387" y="1021" text-anchor="middle" textLength="436" lengthAdjust="spacingAndGlyphs">TO KEEP HIDDEN FOR YEARS!</text>

      <rect class="author-band" x="0" y="1051" width="760" height="89"/>
      <text class="author-name" x="383" y="1113" text-anchor="middle" textLength="450" lengthAdjust="spacing">COLIN MAYHEW</text>
    </svg>
  </main>
</body>
</html>
```